Private launch of Lullo, the smart baby sleep tracker

We need a webpage/website to initiate the Private launch of Lullo, our baby sleep tracker.

Meet Lullo:
Sleep, or rather the lack of sleep, is the one of the most challenging aspect of caring for a newborn in the first year. Recently, phone apps for baby tracking have taken hold. But those continue requiring parents to manually enter sleep and awake time. Sleep-deprived parents need a safe, automatic, accurate and stress-free tracking system. Therefore, we provide an affordable smart wearable to track baby’s sleep based on baby’s vital signs.

Target Market(s)

new parents with infants

Industry/Entity Type

Baby Care

Number of Pages Required

1 page

Font styles to use
Sans Serif

Colors
85cae6
f8ba93

Requirements
Must have
• Lullo baby sleep tracker, demonstration video, payment and ordering information. Introduction of our company "Brindle Works Digital".
• Considering the primary targets are sleep-deprived new parents, the webpage should be user-friendly.
Nice to have
• Product rating and reviews

```html
<!DOCTYPE html>
<html lang="en">
<head>
<meta charset="utf-8">
<title>Brindle Works Digital — Lullo Sleep Tracker</title>
<link href="https://fonts.googleapis.com/css2?family=Montserrat:wght@400;500;600;700&family=Poppins:wght@400;500;600;700&display=swap" rel="stylesheet">
<style>
:root{
  --blue:#85cae6;
  --blue-deep:#2f8fb8;
  --peach:#f8ba93;
  --peach-deep:#e98a52;
  --ink:#2b2f3a;
  --navy:#2f3442;
  --cream:#f7f3ee;
  --band:#eff4f6;
  --field:#eff1f2;
  --dark:#15181d;
  --muted:#555;
}
*{margin:0;padding:0;box-sizing:border-box}
html,body{width:1200px;height:3319px;overflow:hidden}
body{position:relative;background:#fff;font-family:'Montserrat',sans-serif;color:var(--ink)}
.abs{position:absolute}
.heading{font-family:'Poppins',sans-serif}
.btn{position:absolute;background:var(--blue);color:var(--ink);border-radius:30px;font-family:'Poppins',sans-serif;font-weight:600;display:flex;align-items:center;justify-content:center}

/* header */
.header{top:0;left:0;width:1200px;height:101px;background:#fff}
.brand{left:112px;top:20px;display:flex;align-items:center;gap:10px}
.brand-mark{width:26px;height:26px;border-radius:50%;background:var(--blue)}
.brand-name{font-family:'Poppins',sans-serif;font-weight:700;font-size:32px;color:var(--ink);line-height:1}
.brand-sub{left:150px;top:62px;font-size:16px;letter-spacing:20px;color:var(--ink);font-weight:500}
.service{left:910px;top:20px;display:flex;gap:10px;align-items:center}
.service-icon{width:34px;height:34px;border-radius:50%;background:var(--blue);display:flex;align-items:center;justify-content:center}
.service small{display:block;font-size:9px;font-weight:600}
.service b{font-weight:500;font-size:16px}
.nav{right:113px;top:62px;display:flex;gap:29px;font-size:15px;font-weight:500}
.nav .on{color:var(--blue-deep)}

/* hero */
.hero{top:101px;left:0;width:1200px;height:634px;background:linear-gradient(100deg,#4a4a4a,#5c5a58 55%,#6e6862);overflow:hidden}
.hero h1{position:absolute;top:200px;width:100%;text-align:center;font-family:'Poppins',sans-serif;font-size:54px;color:#fff;font-weight:600}
.hero p{position:absolute;top:283px;width:100%;text-align:center;color:#fff;font-weight:700;font-size:15.5px;line-height:26px}
.hero .btn{left:517px;top:356px;width:169px;height:52px;font-size:19px}
.dots{left:1133px;top:275px}
.dots span{display:block;background:#fff;border-radius:50%;margin:0 auto 14px}

/* about */
.about-media{left:134px;top:838px;width:446px;height:294px;border:3px solid var(--navy);background:linear-gradient(135deg,#2e5a5a,#6a8a88 50%,#c8c6c2)}
.about-title{left:623px;top:846px;font-size:40px;font-weight:600}
.about-text{left:623px;top:915px;width:470px;font-size:14.5px;line-height:27.5px;color:#333}
.about .btn{left:622px;top:1071px;width:171px;height:50px;font-size:18px}

/* products */
.products{top:1226px;left:0;width:1200px;height:779px;background:var(--band)}
.section-title{width:100%;text-align:center;font-family:'Poppins',sans-serif;font-weight:600}
.card{top:174px;width:311px;height:486px;background:var(--cream);text-align:center}
.card.dark{background:var(--navy);color:#fff}
.card .year{margin-top:35px;font-family:'Poppins',sans-serif;font-size:26px;font-weight:500;color:var(--blue-deep)}
.card.dark .year{color:#fff}
.shot{width:116px;height:116px;border-radius:50%;margin:14px auto 0;border:4px solid var(--navy)}
.card.dark .shot{border-color:var(--peach)}
.card h3{margin-top:28px;font-family:'Poppins',sans-serif;font-size:20px;font-weight:600;color:var(--blue-deep)}
.card.dark h3{color:var(--blue)}
.card .age{margin-top:12px;font-size:17px;font-weight:500}
.card .desc{margin-top:14px;font-size:17px;line-height:25px}
.card .btn{left:71px;top:396px;width:170px;height:52px;font-size:18px}

/* testimonials */
.stars{top:2190px;left:0;width:1200px;text-align:center;color:var(--peach-deep);font-size:22px;letter-spacing:6px}
.quote{top:2237px;left:220px;width:760px;text-align:center;font-size:15px;line-height:27.5px;color:var(--muted)}
.author{top:2340px;left:0;width:1200px;text-align:center;font-family:'Poppins',sans-serif}
.author b{color:var(--blue-deep);font-weight:600;font-size:19px}
.author em{font-size:14px;color:#444;margin-left:10px}
.arrow{width:54px;height:54px;border-radius:50%;background:var(--blue);display:flex;align-items:center;justify-content:center;top:2236px}

/* contact */
.contact-bg{top:2440px;left:0;width:1200px;height:879px}
.contact-card{left:240px;top:2476px;width:717px;height:453px;background:#fff}
.contact-card h2{position:absolute;top:44px;width:100%;text-align:center;font-family:'Poppins',sans-serif;font-size:46px;font-weight:700}
.field{position:absolute;background:var(--field);border-radius:22px;font-size:13px;color:#555;padding:14px 27px}
.fold{left:240px;top:2872px}
.contact-card .btn{left:265px;top:365px;width:187px;height:51px;font-weight:700;font-size:19px}

.info{top:3010px;color:#fff;display:flex;gap:14px}
.info small{display:block;font-size:10px;font-weight:600;margin-bottom:6px}
.info span{font-size:14px;line-height:24px}
.divider{top:3000px;width:1px;height:84px;background:#333}
.pay{top:3171px;left:441px;display:flex;gap:8px}
.pay i{display:block;width:46px;height:28px;border-radius:4px;background:#e8e8e8;border:2px solid #999}
.social{top:3228px;left:516px;display:flex;gap:6px}
.social i{display:block;width:38px;height:38px;border-radius:50%;border:2px solid #fff}
.copy{top:3282px;width:1200px;text-align:center;color:#fff;font-size:13px}
</style>
</head>
<body>

<header class="abs header">
  <div class="abs brand"><span class="brand-mark"></span><span class="brand-name">Brindle Works</span></div>
  <div class="abs brand-sub">DIGITAL</div>
  <div class="abs service">
    <div class="service-icon"><svg width="18" height="18" viewBox="0 0 24 24" fill="none" stroke="#fff" stroke-width="2"><path d="M5 3h4l2 5-3 2a12 12 0 0 0 6 6l2-3 5 2v4a2 2 0 0 1-2 2A18 18 0 0 1 3 5a2 2 0 0 1 2-2z"/></svg></div>
    <div><small>Customer Service</small><b>(555) 014-2290</b></div>
  </div>
  <nav class="abs nav"><span class="on">Home</span><span>About Us</span><span>Product</span><span>Features</span><span>Testimonial</span><span>Contact Us</span></nav>
</header>

<section class="abs hero" role="img" aria-label="Photo of a sleeping newborn beside a knitted toy">
  <h1>Welcome To Brindle Works Digital</h1>
  <p>Duis aute irure dolor in reprehenderit in voluptate velit esse cillum dolore eu<br>fugiat nulla pariatur. Excepteur sint occaecat cupidatat non</p>
  <div class="btn">Buy Now</div>
  <div class="abs dots">
    <span style="width:28px;height:28px;background:none;border:3px solid #fff;position:relative"><span style="position:absolute;left:6px;top:6px;width:10px;height:10px;margin:0"></span></span>
    <span style="width:14px;height:14px"></span>
    <span style="width:14px;height:14px"></span>
  </div>
  <svg class="abs" style="left:0;top:0" width="1200" height="634" viewBox="0 0 1200 634">
    <path d="M0,624 C60,540 120,531 187,531 C320,531 480,634 600,634 C720,634 880,531 1057,531 C1130,531 1170,560 1200,600 L1200,640 L0,640 Z" fill="#fff"/>
    <path d="M0,624 C60,540 120,531 187,531 C320,531 480,634 600,634 C720,634 880,531 1057,531 C1130,531 1170,560 1200,600" fill="none" stroke="var(--peach)" stroke-width="5"/>
  </svg>
</section>

<section class="about">
  <div class="abs about-media" role="img" aria-label="Demonstration video still of a sleeping baby">
    <svg class="abs" style="left:188px;top:110px" width="70" height="70" viewBox="0 0 70 70"><circle cx="35" cy="35" r="32" fill="none" stroke="#fff" stroke-width="3"/><path d="M28 22 L49 35 L28 48 Z" fill="none" stroke="#fff" stroke-width="3"/></svg>
  </div>
  <h2 class="abs about-title heading">About Us</h2>
  <p class="abs about-text">Nunc id turpis ligula. Orci varius natoque penatibus et magnis disparmontes, nascetur ridiculus mus. Nulla eu ligula vitae risus varius tincidunacus aliquet vitae aliquet ut, elementum a massa. Pellentesqu elit libero, fermentum met porta ac, fringilla at erat. Nunc bibendum enim vel arcu rutrum semper</p>
  <div class="btn">Read More</div>
</section>

<section class="abs products">
  <h2 class="abs section-title" style="top:72px;font-size:40px">Products</h2>
  <div class="abs card" style="left:116px">
    <div class="year">2019</div>
    <div class="shot" role="img" aria-label="Product photo of the lilac Lullo Sleep Tracker band" style="background:radial-gradient(circle,#e2b8e6,#f4f0f4 70%)"></div>
    <h3>LULLO SLEEP TRACKER</h3>
    <div class="age">0-1 month</div>
    <div class="desc">Assistant for<br>postpartum doula</div>
    <div class="btn">Add To Cart</div>
  </div>
  <div class="abs card dark" style="left:451px">
    <div class="year">2020</div>
    <div class="shot" role="img" aria-label="Product photo of the white Lullo Sleep Tracker+ band" style="background:radial-gradient(circle,#e4e4e0,#fafafa 70%)"></div>
    <h3>LULLO SLEEP TRACKER+</h3>
    <div class="age">2-18 month</div>
    <div class="desc">First in market,<br>Smart &amp; Affordable</div>
    <div class="btn">Add To Cart</div>
  </div>
  <div class="abs card" style="left:786px">
    <div class="year">2020</div>
    <div class="shot" role="img" aria-label="Product photo of the mint Lullo Sleep Tracker MD band" style="background:radial-gradient(circle,#a6e4b6,#f2f7f3 70%)"></div>
    <h3>LULLO SLEEP TRACKER MD</h3>
    <div class="age">2-18 month</div>
    <div class="desc">Tailored for<br>Pediatricians</div>
    <div class="btn">Add To Cart</div>
  </div>
</section>

<section class="testimonials">
  <h2 class="abs section-title" style="top:2104px;left:0;font-size:48px;font-weight:700;color:#111">Testimonials</h2>
  <div class="abs stars">★★★★★</div>
  <p class="abs quote">Sed ut perspiciatis unde omnis iste natus error sit voluptatem accusantium doloremque laudantium, totam rem aperiam, eaque ipsa quae ab illo inventore veritatis et quasi architecto beatae vitae dicta sunt explicabo. Nemo enim ipsam voluptatem quia voluptas sit aspernatur aut</p>
  <div class="abs author"><b>Clara Hendricks</b><em>/ USA</em></div>
  <div class="abs arrow" style="left:85px"><svg width="16" height="16" viewBox="0 0 16 16"><path d="M11 2 L5 8 L11 14" fill="none" stroke="#fff" stroke-width="2.5"/></svg></div>
  <div class="abs arrow" style="left:1061px"><svg width="16" height="16" viewBox="0 0 16 16"><path d="M5 2 L11 8 L5 14" fill="none" stroke="#fff" stroke-width="2.5"/></svg></div>
</section>

<section class="contact">
  <svg class="abs contact-bg" width="1200" height="879" viewBox="0 0 1200 879" role="img" aria-label="Dark photo backdrop of a resting baby">
    <defs><linearGradient id="darkbg" x1="0" y1="0" x2="1" y2="1"><stop offset="0" stop-color="#0b0b0b"/><stop offset=".6" stop-color="#1a1613"/><stop offset="1" stop-color="#0e0d0c"/></linearGradient></defs>
    <path d="M0,118 C30,140 80,155 140,150 C200,145 240,125 300,100 L900,100 C960,75 1010,67 1057,67 C1110,67 1160,90 1200,118 L1200,879 L0,879 Z" fill="url(#darkbg)"/>
    <path d="M0,118 C30,140 80,155 140,150 C200,145 240,125 300,100 M900,100 C960,75 1010,67 1057,67 C1110,67 1160,90 1200,118" fill="none" stroke="var(--peach)" stroke-width="5"/>
  </svg>
  <div class="abs contact-card">
    <h2>Contact Us</h2>
    <div class="field" style="left:72px;top:169px;width:179px;height:43px">Name</div>
    <div class="field" style="left:269px;top:169px;width:179px;height:43px">Email</div>
    <div class="field" style="left:465px;top:169px;width:179px;height:43px">Phone</div>
    <div class="field" style="left:72px;top:231px;width:572px;height:107px">Message</div>
    <div class="btn">SUBMIT</div>
  </div>
  <svg class="abs fold" width="57" height="57" viewBox="0 0 57 57"><path d="M0 0 H57 V57 Z" fill="var(--peach)"/></svg>

  <div class="abs info" style="left:190px">
    <svg width="30" height="48" viewBox="0 0 30 48" fill="none" stroke="#fff" stroke-width="2.5"><rect x="2" y="2" width="26" height="44" rx="4"/><line x1="11" y1="40" x2="19" y2="40"/></svg>
    <div><small>Call Us</small><span>(555)-014 2290</span></div>
  </div>
  <div class="abs divider" style="left:387px"></div>
  <div class="abs info" style="left:430px">
    <svg width="54" height="52" viewBox="0 0 54 52" fill="none" stroke="#fff" stroke-width="2"><path d="M27 44 C17 30 13 24 13 17 a14 14 0 0 1 28 0 c0 7 -4 13 -14 27z"/><circle cx="27" cy="17" r="5"/><path d="M16 36 C5 38 2 42 6 45 C14 51 40 51 48 45 C52 42 49 38 38 36"/></svg>
    <div><small>Address</small><span>#10, Duis aute irure dolor in<br>reprehenderit in voluptate</span></div>
  </div>
  <div class="abs divider" style="left:754px"></div>
  <div class="abs info" style="left:800px">
    <svg width="54" height="40" viewBox="0 0 54 40" fill="none" stroke="#fff" stroke-width="2.5"><rect x="2" y="2" width="50" height="36" rx="2"/><path d="M2 2 L27 22 L52 2 M2 38 L20 17 M52 38 L34 17"/></svg>
    <div><small>Email</small><span>info@brindleworksdigital.com</span></div>
  </div>

  <div class="abs pay" aria-label="Accepted payment methods"><i></i><i></i><i></i><i></i><i></i><i></i></div>
  <div class="abs social" aria-label="Social links"><i></i><i></i><i></i><i></i></div>
  <div class="abs copy">© Copyrights 2019 | All Rights Reserved</div>
</section>

</body>
</html>
```